Dr. Marissa Tevlin Medical/Chiropractic Business Card

Dr. Tevlin is a chiropractor and will require a business card that she uses every single day to book appointments on the back side of the card. Currently the office name goes by Dr. Marissa Tevlin. The chiropractic profession is based on the diagnosis and manipulative treatment of misalignments of the joints, especially those of the spinal column, which are held to cause other disorders by affecting the nerves, muscles, and organs. Dr. Marissa Tevlin is looking for a contemporary and minimalistic design.

Industry/Entity Type

Medical

Contact Information for Business Card

Name: Dr. Marissa Tevlin; Address: 748 Harcastle Rd South, London, ON N5R 2K7; Phone Number: 519.274.6193; Fax: 519.281.5046; email: marissa.tevlin@quorvamail.com

Requirements
Must have
• ability to write multiple appointments date/time on the back of card

```html
<!DOCTYPE html>
<html lang="en">
<head>
<meta charset="utf-8">
<title>Dr. Marissa Tevlin – Business Card</title>
<link rel="stylesheet" href="https://fonts.googleapis.com/css2?family=Roboto+Condensed:wght@700&family=Roboto:wght@300;400;500;700&family=Noto+Serif:ital,wght@1,700&display=swap">
<style>
  :root {
    --backdrop-center: #4e4e4e;
    --backdrop-edge: #111111;
    --brand-blue-light: #0e5b96;
    --brand-blue-dark: #0a3f72;
    --panel-white: #f4f5f6;
    --panel-shadow: #061c33;
    --ink: #111111;
    --paper: #ffffff;
    --spine-tone: #c3cadb;
  }
  * { margin: 0; padding: 0; box-sizing: border-box; }
  html, body { width: 999px; height: 1200px; overflow: hidden; }
  body {
    position: relative;
    background: radial-gradient(ellipse at 50% 45%, var(--backdrop-center) 0%, #2c2c2c 60%, var(--backdrop-edge) 100%);
    font-family: "Roboto", Arial, sans-serif;
    color: var(--ink);
  }

  /* ---------- Front of card ---------- */
  .card-front {
    position: absolute; left: 48px; top: 85px; width: 910px; height: 520px;
    background: linear-gradient(180deg, var(--brand-blue-light) 0%, var(--brand-blue-dark) 100%);
  }
  .identity { position: absolute; left: 50px; top: 192px; color: var(--paper); }
  .identity .title { font-weight: 300; font-size: 31px; line-height: 1; letter-spacing: 0.5px; }
  .identity .name {
    font-family: "Roboto Condensed", "Arial Narrow", sans-serif;
    font-weight: 700; font-size: 60px; line-height: 1; margin-top: 12px; letter-spacing: 0.5px;
  }
  .identity .profession { font-weight: 300; font-size: 34px; line-height: 1; margin-top: 14px; letter-spacing: 0.5px; }

  .info-panel {
    position: absolute; right: 0; background: var(--panel-white);
    box-shadow: -4px 4px 0 var(--panel-shadow);
  }
  .info-panel.address { top: 99px; width: 403px; height: 116px; }
  .info-panel.contact { top: 243px; width: 403px; height: 174px; }
  .info-row { position: absolute; left: 24px; display: flex; align-items: center; }
  .info-row svg { flex: none; }
  .info-row .text { margin-left: 18px; font-size: 23px; line-height: 31px; }
  .address .info-row { top: 24px; }
  .phone-main { top: 32px; }
  .phone-main .text { font-weight: 700; font-size: 34px; }
  .fax { top: 82px; }
  .email { top: 120px; }
  .fax .text, .email .text { font-size: 22px; }

  /* ---------- Back of card ---------- */
  .card-back {
    position: absolute; left: 42px; top: 628px; width: 910px; height: 520px;
    background: var(--paper);
  }
  .back-header {
    height: 134px;
    background: linear-gradient(90deg, var(--brand-blue-light) 0%, var(--brand-blue-dark) 100%);
    display: flex; align-items: center; justify-content: center;
  }
  .back-header h1 {
    font-family: "Noto Serif", Georgia, serif; font-style: italic; font-weight: 700;
    font-size: 66px; color: var(--paper); letter-spacing: 1px; margin-top: 8px;
  }
  .spine-art {
    position: absolute; left: 430px; top: 140px; width: 80px; height: 292px;
    border-radius: 40px 40px 30px 30px;
    background: linear-gradient(180deg, rgba(195,202,219,0.15), var(--spine-tone) 50%, rgba(195,202,219,0.2));
  }
  .column-label { position: absolute; top: 168px; font-weight: 700; font-size: 30px; transform: translateX(-50%); }
  .column-label.date { left: 255px; }
  .column-label.time { left: 665px; }
  .write-line { position: absolute; height: 3px; background: var(--ink); }
  .write-line.left { left: 74px; width: 353px; }
  .write-line.right { left: 483px; width: 353px; }
  .reschedule-note {
    position: absolute; left: 0; right: 0; top: 436px; text-align: center;
    font-weight: 700; font-size: 23px; line-height: 30px;
  }
</style>
</head>
<body>

<section class="card-front">
  <div class="identity">
    <p class="title">DR.</p>
    <p class="name">MARISSA TEVLIN</p>
    <p class="profession">CHIROPRACTOR</p>
  </div>

  <div class="info-panel address">
    <div class="info-row">
      <svg width="22" height="36" viewBox="0 0 22 36" aria-hidden="true">
        <path d="M11 1C5.5 1 1 5.4 1 10.8 1 18 11 35 11 35s10-17 10-24.2C21 5.4 16.5 1 11 1z" fill="#111"/>
        <circle cx="11" cy="10.5" r="4.2" fill="#f4f5f6"/>
      </svg>
      <p class="text">748 Harcastle Rd South<br>London, ON N5R 2K7</p>
    </div>
  </div>

  <div class="info-panel contact">
    <div class="info-row phone-main">
      <svg width="24" height="24" viewBox="0 0 24 24" aria-hidden="true">
        <path d="M6.6 10.8c1.4 2.8 3.8 5.1 6.6 6.6l2.2-2.2c.3-.3.7-.4 1-.2 1.1.4 2.3.6 3.6.6.6 0 1 .4 1 1V20c0 .6-.4 1-1 1C10.6 21 3 13.4 3 4c0-.6.4-1 1-1h3.5c.6 0 1 .4 1 1 0 1.3.2 2.5.6 3.6.1.3 0 .7-.2 1L6.6 10.8z" fill="#111"/>
        <path d="M14 3a7 7 0 0 1 7 7M14 6.5a3.5 3.5 0 0 1 3.5 3.5" stroke="#111" stroke-width="1.8" fill="none"/>
      </svg>
      <p class="text">519.274.6193</p>
    </div>
    <div class="info-row fax">
      <svg width="24" height="22" viewBox="0 0 24 22" aria-hidden="true">
        <rect x="5" y="1" width="14" height="7" fill="#111"/>
        <rect x="1" y="9" width="22" height="9" rx="1" fill="#111"/>
        <rect x="5" y="12" width="14" height="2" fill="#f4f5f6"/>
        <rect x="1" y="19" width="22" height="3" fill="#111"/>
      </svg>
      <p class="text">519.281.5046</p>
    </div>
    <div class="info-row email">
      <svg width="24" height="22" viewBox="0 0 24 22" aria-hidden="true">
        <path d="M1 9l11-8 11 8v12H1z" fill="#111"/>
        <path d="M1 9l11 7 11-7" stroke="#f4f5f6" stroke-width="1.6" fill="none"/>
      </svg>
      <p class="text">marissa.tevlin@quorvamail.com</p>
    </div>
  </div>
</section>

<section class="card-back">
  <header class="back-header"><h1>APPOINTMENTS</h1></header>

  <div class="spine-art" role="img" aria-label="Faint spine illustration"></div>

  <p class="column-label date">Date</p>
  <p class="column-label time">Time</p>

  <div class="write-line left" style="top:233px"></div>
  <div class="write-line left" style="top:284px"></div>
  <div class="write-line left" style="top:336px"></div>
  <div class="write-line left" style="top:387px"></div>
  <div class="write-line right" style="top:233px"></div>
  <div class="write-line right" style="top:284px"></div>
  <div class="write-line right" style="top:336px"></div>
  <div class="write-line right" style="top:387px"></div>

  <p class="reschedule-note">If you are unable to make your appointment,<br>Please call us to reschedule</p>
</section>

</body>
</html>
```